Professional and creatice Life Coach - Business Card design

I just relaunched my website and now i a need a correspoonding business card for my task as life coach. My website is www.tbalrond.com as reference. The compass is kind of a symbol for my work, as I help people navigate through their challenging phases in life. The business card should be colorful, but not too playful as I also adress business people. So it sould be creative, but professional (also to suport my other business as Management Consultant)

Target Market(s)

People who want to get teir problems resolved, in business, partnership and other personal realms

Industry/Entity Type

Life Coaching

Contact Information for Business Card

Front side should include Name, Phone number, Email, Website and address

Font styles to use
Sans Serif

Colors
add136

Requirements
Must have
• "Mag. Leopold Brantner" -> Name
"Energetische Praxis" -> Jobtitle (describing my profession as life coach)
colours and style should match my website www.tbalrond.com
Nice to have
• a compass as a symbol

```html
<!DOCTYPE html>
<html lang="de">
<head>
<meta charset="utf-8">
<title>Energetische Praxis – Visitenkarte</title>
<link href="https://fonts.googleapis.com/css2?family=Cormorant+Garamond:wght@500;600&family=Montserrat:wght@400;600&display=swap" rel="stylesheet">
<style>
  :root {
    --brand-green: #add136;
    --brand-green-light: #c4da93;
    --ink: #4a4a4a;
    --paper: #ffffff;
    --backdrop: #e4e1dc;
    --mark-tint: #eef5d8;
  }
  * { margin: 0; padding: 0; box-sizing: border-box; }
  html, body { width: 1200px; height: 965px; overflow: hidden; background: var(--backdrop); }
  .card {
    position: absolute;
    border-radius: 24px;
    overflow: hidden;
  }
  .card--front {
    left: 272px; top: 90px; width: 656px; height: 376px;
    background: var(--brand-green);
  }
  .front-badge {
    position: absolute; left: 268px; top: 82px;
    width: 120px; height: 120px; border-radius: 50%;
    border: 3px solid var(--paper);
  }
  .front-name {
    position: absolute; left: 0; right: 0; top: 230px;
    text-align: center; color: var(--paper);
    font-family: 'Cormorant Garamond', serif; font-weight: 600;
    font-size: 33px; line-height: 39px; letter-spacing: 0.5px;
    text-transform: uppercase;
  }
  .card--back {
    left: 278px; top: 503px; width: 647px; height: 369px;
    background: var(--paper);
  }
  .holder-name {
    position: absolute; left: 28px; top: 22px;
    font-family: 'Cormorant Garamond', serif; font-weight: 600;
    font-size: 25px; color: var(--brand-green);
  }
  .holder-role {
    position: absolute; left: 29px; top: 58px;
    font-family: 'Cormorant Garamond', serif; font-weight: 500;
    font-size: 17px; color: var(--ink);
  }
  .practice {
    position: absolute; left: 26px; top: 162px;
    font-family: 'Montserrat', sans-serif;
  }
  .practice-title { font-weight: 600; font-size: 14px; color: var(--brand-green); letter-spacing: 0.3px; }
  .practice-address { font-size: 14px; color: var(--ink); margin-top: 7px; }
  .contact-list {
    position: absolute; left: 26px; top: 244px; list-style: none;
    font-family: 'Montserrat', sans-serif; font-size: 18px; color: var(--ink);
  }
  .contact-list li { display: flex; align-items: center; height: 23.3px; }
  .contact-list svg { width: 18px; height: 18px; margin-right: 14px; flex: none; }
  .back-mark {
    position: absolute; left: 356px; top: 65px;
    width: 240px; height: 240px; border-radius: 50%;
    background: var(--mark-tint);
  }
  .footer-band { position: absolute; left: 0; bottom: 0; width: 647px; height: 14px; }
</style>
</head>
<body>
  <section class="card card--front">
    <div class="front-badge"></div>
    <h1 class="front-name">Energetische Praxis<br>Leopold Brantner</h1>
  </section>

  <section class="card card--back">
    <h2 class="holder-name">Mag. Leopold Brantner</h2>
    <p class="holder-role">Life Coach</p>

    <div class="practice">
      <p class="practice-title">ENERGETISCHE PRAXIS</p>
      <p class="practice-address">Lindenweg 12, 5020 Salzburg</p>
    </div>

    <ul class="contact-list">
      <li>
        <svg viewBox="0 0 24 24" aria-hidden="true"><path fill="#add136" d="M6.6 10.8a15 15 0 0 0 6.6 6.6l2.2-2.2c.3-.3.7-.4 1-.2 1.1.4 2.3.6 3.6.6.6 0 1 .4 1 1V20c0 .6-.4 1-1 1A17 17 0 0 1 3 4c0-.6.4-1 1-1h3.5c.6 0 1 .4 1 1 0 1.3.2 2.5.6 3.6.1.3 0 .7-.2 1z"/></svg>
        +43 664 3819042
      </li>
      <li>
        <svg viewBox="0 0 24 24" aria-hidden="true"><rect x="6" y="1.5" width="12" height="21" rx="2.5" fill="none" stroke="#add136" stroke-width="2"/><circle cx="12" cy="18.5" r="1.3" fill="#add136"/></svg>
        +43 664 3819042
      </li>
      <li>
        <svg viewBox="0 0 24 24" aria-hidden="true"><path fill="#add136" d="M2 5h20v14H2z"/><path fill="none" stroke="#fff" stroke-width="1.6" d="M2 5l10 8 10-8"/></svg>
        info@tbalrond.com
      </li>
      <li>
        <svg viewBox="0 0 24 24" aria-hidden="true"><circle cx="12" cy="12" r="10" fill="#add136"/><path fill="none" stroke="#fff" stroke-width="1.3" d="M2 12h20M12 2c3 3 3 17 0 20M12 2c-3 3-3 17 0 20"/></svg>
        www.tbalrond.com
      </li>
    </ul>

    <div class="back-mark"></div>

    <svg class="footer-band" viewBox="0 0 647 14" aria-hidden="true">
      <polygon points="0,0 408,0 394,14 0,14" fill="var(--brand-green)"/>
      <polygon points="414,0 647,0 647,14 400,14" fill="var(--brand-green-light)"/>
    </svg>
  </section>
</body>
</html>
```